Pelmoro Travel

We are new traveling company from Italy and looking for a really unique design as soon as possible of the main page.
Travel is an online business. We all do online research before taking a vacation. Since some of us will spend hours researching a trip before finally booking it on a travel website, design is critical.
People looking to travel are going to start with an idea. Some may be browsing for a specific type of trip (river cruise, kayaking, etc.) while others may be looking at specific dates (i.e. February). Still others are considering going to a specific destination such as the Grand Canyon, but all of these visitors are goal-oriented. This type of visitor is frustrated by not finding thle right information easily. This is why travel web design must offer several ways to navigate such as by date, location, activity, cost, etc.
The design should be easy to use for visitors, look fantastic and be easy to update and maintain.
Uploaded some sample pictures but feel free to use your own if it looks good. About colors, blue and white would mix great.

Our future address will be pelmorotravel.com

```html
<!DOCTYPE html>
<html lang="en">
<head>
<meta charset="utf-8">
<title>Pelmoro Travel</title>
<link href="https://fonts.googleapis.com/css2?family=Open+Sans:wght@400;600;700&display=swap" rel="stylesheet">
<style>
:root{
  --blue:#1e5d91;
  --blue-dark:#2c5d8c;
  --cyan:#3cb4e6;
  --orange:#e9a21a;
  --hot:#f26a21;
  --ink:#333;
  --muted:#7a7a7a;
  --line:#e3e3e3;
  --panel:#f4f4f4;
  --black:#111;
}
*{box-sizing:border-box;margin:0;padding:0}
html,body{width:1200px;height:2372px;overflow:hidden;background:#fff;font-family:'Open Sans',sans-serif;color:var(--ink)}
.page{position:relative;width:1200px;height:2372px}
.abs{position:absolute}

/* hero */
.hero{left:0;top:0;width:1200px;height:404px;background:linear-gradient(180deg,#2f7fa8 0%,#25a6c8 45%,#1bb6c9 75%,#2c8fa0 100%)}
.brand{left:79px;top:216px;width:240px;height:188px;background:#fff;display:flex;align-items:center;padding-left:24px;font-family:'Open Sans',sans-serif;font-weight:700;font-size:26px;color:var(--blue);white-space:nowrap}
.offer{left:319px;top:216px;width:269px;height:188px;background:var(--black);color:#fff;padding:18px 0 0 24px}
.offer h2{font-size:34px;font-weight:600;color:var(--hot);letter-spacing:1px}
.offer h2 small{font-size:17px;color:#ddd;font-weight:400;letter-spacing:0;margin-left:8px}
.offer p{font-size:18px;line-height:28px;margin-top:12px;font-weight:600}
.offer p.meta{font-size:15px;margin-top:10px}
.corner{right:0;bottom:0;width:0;height:0;border-left:64px solid transparent;border-bottom:64px solid var(--hot)}
.corner-text{right:4px;bottom:10px;transform:rotate(-45deg);font-size:10px;font-weight:700;color:#111;line-height:11px;text-align:center}
.hero-nav{top:357px;width:56px;height:47px;display:flex;align-items:center;justify-content:center}
.hero-nav.prev{left:941px;background:#333}
.hero-nav.next{left:997px;background:#fff}

/* nav */
.mainnav{left:81px;top:446px;width:1036px;height:57px;border-bottom:2px solid var(--line);display:flex;align-items:flex-start}
.mainnav a{font-size:17px;color:#444;text-decoration:none;padding:0 28px;border-left:1px solid #ddd;line-height:32px}
.mainnav a:first-child{padding-left:10px;border-left:none}
.social-mini{right:0;top:12px;display:flex;gap:20px}
.social-mini span{width:9px;height:9px;border-radius:50%;background:#888}

/* search */
.search{left:81px;top:554px;width:1036px;height:291px;border:1px solid #e2e2e2;box-shadow:0 2px 6px rgba(0,0,0,.15);background:#fff}
.col{top:22px}
.col h3{font-size:31px;font-weight:700;color:var(--blue)}
.col h3 b{color:var(--orange)}
.col label{display:block;font-size:15px;color:var(--muted);margin-top:24px}
.field{margin-top:8px;height:42px;border:1px solid #d3d3d3;font-size:14px;color:#777;padding:0 12px;display:flex;align-items:center;justify-content:space-between}
.radio{display:flex;align-items:center;gap:12px;font-size:16px;color:#555;margin-top:14px}
.radio i{width:14px;height:14px;border:1px solid #bbb;border-radius:50%;display:inline-block}
.radio i.on{background:radial-gradient(circle,#999 0 3px,#fff 4px)}
.send{left:430px;top:276px;height:34px;display:flex}
.btn-label{background:var(--cyan);color:#fff;font-size:14px;font-weight:600;padding:0 14px;line-height:34px;letter-spacing:.5px}
.btn-arrow{width:34px;background:var(--blue-dark);display:flex;align-items:center;justify-content:center}

/* categories */
.section-title{font-size:27px;font-weight:400;color:var(--blue)}
.pager{top:944px;display:flex;gap:6px}
.pager span{width:40px;height:40px;border:1px solid #ddd;display:flex;align-items:center;justify-content:center}
.card{top:1020px;width:306px}
.card .photo{height:210px}
.card h4{font-size:19px;font-weight:600;color:var(--blue);margin-top:22px}
.card p{font-size:14px;line-height:29px;color:#666;margin-top:6px}
.card .book{display:flex;height:37px;margin-top:20px}
.card .book .btn-label{width:148px;text-align:center;line-height:37px}

/* deals */
.deal{left:81px;width:640px}
.deal .photo{width:214px;height:160px;border:5px solid #fff;box-shadow:0 1px 5px rgba(0,0,0,.3)}
.deal h4{left:242px;top:0;font-size:21px;font-weight:400;color:#111;font-family:Arial,sans-serif}
.deal p{left:242px;top:42px;width:400px;font-size:14px;line-height:27px;color:#555}
.stars{left:242px;top:126px;display:flex;gap:3px}
.catlist{left:808px;top:1532px;width:309px;list-style:none}
.catlist li{height:45px;border-bottom:1px solid var(--line);font-size:16px;color:#555;display:flex;align-items:center;gap:14px;padding-left:4px}
.catlist li:nth-child(5){margin-bottom:9px}

/* footer */
.footer{left:0;top:1972px;width:1200px;height:319px;background:var(--panel)}
.footer .section-title{font-size:26px}
.about p{font-size:14px;line-height:26px;color:#555;width:370px;margin-top:18px}
.news-item{display:flex;gap:20px;margin-top:26px}
.news-item .thumb{width:70px;height:66px}
.news-item b{display:block;font-size:14px;font-weight:600;color:var(--blue)}
.news-item span{display:block;font-size:13px;line-height:23px;color:#777}
.follow address{font-style:normal;font-size:17px;color:#555;margin-top:24px}
.follow .phone{font-size:22px;color:var(--cyan);margin-top:10px}
.follow .dots{display:flex;gap:22px;margin-top:22px}
.follow .dots span{width:40px;height:40px;border-radius:50%}
.bottom{left:81px;top:2318px;width:1036px;display:flex;justify-content:space-between;font-size:16px;color:#333}
</style>
</head>
<body>
<div class="page">

  <header>
    <div class="abs hero" role="img" aria-label="Overwater bungalows on a turquoise lagoon"></div>
    <div class="abs brand">Pelmoro Travel</div>
    <div class="abs offer">
      <h2>HAWAI:<small>FROM $569</small></h2>
      <p>LONDON, DUBLIN,<br>EDINBURG</p>
      <p class="meta">6-7 NIGHTS, AIRFARE</p>
      <div class="abs corner"></div>
      <div class="abs corner-text">SIGN UP<br>NOW!</div>
    </div>
    <div class="abs hero-nav prev"><svg width="14" height="24" viewBox="0 0 14 24"><path d="M12 2 2 12l10 10" fill="none" stroke="#fff" stroke-width="2"/></svg></div>
    <div class="abs hero-nav next"><svg width="14" height="24" viewBox="0 0 14 24"><path d="M2 2l10 10L2 22" fill="none" stroke="#999" stroke-width="2"/></svg></div>
  </header>

  <nav class="abs mainnav">
    <a href="#">HOME</a><a href="#">ACTIVITIES</a><a href="#">TOURS</a><a href="#">HOTELS</a><a href="#">COST</a><a href="#">CONTACTS</a>
    <div class="abs social-mini"><span></span><span></span><span></span></div>
  </nav>

  <section class="abs search">
    <div class="abs col" style="left:26px;width:170px">
      <h3><b>01.</b>Date</h3>
      <label>Check-in date</label>
      <div class="field">20/05/2014 <svg width="20" height="16"><rect x="1" y="2" width="18" height="13" fill="none" stroke="#aaa"/><path d="M1 6h18M6 6v9M10 6v9M14 6v9M1 10h18" stroke="#ccc"/></svg></div>
      <label style="margin-top:14px">Check-in date</label>
      <div class="field">20/05/2014 <svg width="20" height="16"><rect x="1" y="2" width="18" height="13" fill="none" stroke="#aaa"/><path d="M1 6h18M6 6v9M10 6v9M14 6v9M1 10h18" stroke="#ccc"/></svg></div>
    </div>
    <div class="abs col" style="left:280px;width:184px">
      <h3><b>02.</b>Location</h3>
      <label>Destination</label>
      <div class="field"></div>
      <label style="margin-top:14px">Your e-mail</label>
      <div class="field"></div>
    </div>
    <div class="abs col" style="left:555px;width:200px">
      <h3><b>03.</b>Activity</h3>
      <div class="radio" style="margin-top:20px"><i class="on"></i>River Cruise</div>
      <div class="radio"><i></i>kayaking</div>
      <div class="radio"><i></i>Trekking</div>
      <div class="radio"><i></i>Cycling</div>
      <div class="radio"><i></i>Boating</div>
    </div>
    <div class="abs col" style="left:825px;width:184px">
      <h3><b>02.</b>Cost</h3>
      <label>Minimum</label>
      <div class="field">$ 104 <svg width="12" height="7"><path d="M0 0h12L6 7z" fill="#666"/></svg></div>
      <label style="margin-top:14px">Maximum</label>
      <div class="field">$ 2456K <svg width="12" height="7"><path d="M0 0h12L6 7z" fill="#666"/></svg></div>
    </div>
    <div class="abs send"><span class="btn-label">SEND A REQUEST</span><span class="btn-arrow"><svg width="8" height="12"><path d="M0 0l8 6-8 6z" fill="#fff"/></svg></span></div>
  </section>

  <section>
    <h2 class="abs section-title" style="left:81px;top:945px">TRAVEL CATEGORIES</h2>
    <div class="abs pager" style="left:1025px">
      <span><svg width="8" height="12"><path d="M7 1 2 6l5 5" fill="none" stroke="#333" stroke-width="2"/></svg></span>
      <span><svg width="8" height="12"><path d="M1 1l5 5-5 5" fill="none" stroke="#333" stroke-width="2"/></svg></span>
    </div>
    <article class="abs card" style="left:81px">
      <div class="photo" role="img" aria-label="Passenger airliner in a blue sky" style="background:linear-gradient(180deg,#3f7fc4,#8db4dc 70%,#c9d8ea)"></div>
      <h4>AIRLINE TICKETS</h4>
      <p>Lorem ipsum dolor sit amet consectetuer adi piscing elit Nam cursus Morbi ut mi. Nullam</p>
      <div class="book"><span class="btn-label">BOOK NOW</span><span class="btn-arrow"><svg width="8" height="12"><path d="M0 0l8 6-8 6z" fill="#fff"/></svg></span></div>
    </article>
    <article class="abs card" style="left:447px">
      <div class="photo" role="img" aria-label="Hotel terrace with armchairs by a pool at sunset" style="background:linear-gradient(160deg,#c98b52,#6b4a35 55%,#3a2b24)"></div>
      <h4>HOTELS</h4>
      <p>Lorem ipsum dolor sit amet consectetuer adi piscing elit Nam cursus Morbi ut mi. Nullam</p>
      <div class="book"><span class="btn-label">BOOK NOW</span><span class="btn-arrow"><svg width="8" height="12"><path d="M0 0l8 6-8 6z" fill="#fff"/></svg></span></div>
    </article>
    <article class="abs card" style="left:809px">
      <div class="photo" role="img" aria-label="White cruise ship on open sea" style="background:linear-gradient(180deg,#2a8fd0,#4fb0e0 50%,#1b7fb7)"></div>
      <h4>CRUISES</h4>
      <p>Lorem ipsum dolor sit amet consectetuer adi piscing elit Nam cursus Morbi ut mi. Nullam</p>
      <div class="book"><span class="btn-label">BOOK NOW</span><span class="btn-arrow"><svg width="8" height="12"><path d="M0 0l8 6-8 6z" fill="#fff"/></svg></span></div>
    </article>
  </section>

  <section>
    <h2 class="abs section-title" style="left:81px;top:1477px">HOT DEALS</h2>
    <article class="abs deal" style="top:1544px">
      <div class="photo" role="img" aria-label="Hotel room with beds and warm lighting" style="background:linear-gradient(150deg,#d9b483,#9b6a3e 60%,#5c3b22)"></div>
      <h4 class="abs">Quisque sagittis semper felis condimt</h4>
      <p class="abs">Duis autem vel eum iriure dolor in hendreritvulputate velit esse molestie consequat, vnllum dolore eu feugiat nulla fac ilisis at vero eros accumsan et iusto odio dignissim.</p>
      <div class="abs stars"><svg width="100" height="18" viewBox="0 0 100 18"><g fill="none" stroke="#e9a21a"><path d="M9 1l2.4 5.3 5.6.5-4.3 3.8 1.3 5.6L9 13.3 4 16.2l1.3-5.6L1 6.8l5.6-.5z" fill="#e9a21a"/><path transform="translate(20)" d="M9 1l2.4 5.3 5.6.5-4.3 3.8 1.3 5.6L9 13.3 4 16.2l1.3-5.6L1 6.8l5.6-.5z"/><path transform="translate(40)" d="M9 1l2.4 5.3 5.6.5-4.3 3.8 1.3 5.6L9 13.3 4 16.2l1.3-5.6L1 6.8l5.6-.5z"/><path transform="translate(60)" d="M9 1l2.4 5.3 5.6.5-4.3 3.8 1.3 5.6L9 13.3 4 16.2l1.3-5.6L1 6.8l5.6-.5z"/><path transform="translate(80)" d="M9 1l2.4 5.3 5.6.5-4.3 3.8 1.3 5.6L9 13.3 4 16.2l1.3-5.6L1 6.8l5.6-.5z"/></g></svg></div>
    </article>
    <article class="abs deal" style="top:1737px">
      <div class="photo" role="img" aria-label="Resort bungalows over water at dusk" style="background:linear-gradient(180deg,#2b4f8f,#4b7ec0 55%,#1d3c6e)"></div>
      <h4 class="abs">Quisque sagittis semper felis condimt</h4>
      <p class="abs">Duis autem vel eum iriure dolor in hendreritvulputate velit esse molestie consequat, vnllum dolore eu feugiat nulla fac ilisis at vero eros accumsan et iusto odio dignissim.</p>
      <div class="abs stars"><svg width="100" height="18" viewBox="0 0 100 18"><g fill="none" stroke="#e9a21a"><path d="M9 1l2.4 5.3 5.6.5-4.3 3.8 1.3 5.6L9 13.3 4 16.2l1.3-5.6L1 6.8l5.6-.5z" fill="#e9a21a"/><path transform="translate(20)" d="M9 1l2.4 5.3 5.6.5-4.3 3.8 1.3 5.6L9 13.3 4 16.2l1.3-5.6L1 6.8l5.6-.5z"/><path transform="translate(40)" d="M9 1l2.4 5.3 5.6.5-4.3 3.8 1.3 5.6L9 13.3 4 16.2l1.3-5.6L1 6.8l5.6-.5z"/><path transform="translate(60)" d="M9 1l2.4 5.3 5.6.5-4.3 3.8 1.3 5.6L9 13.3 4 16.2l1.3-5.6L1 6.8l5.6-.5z"/><path transform="translate(80)" d="M9 1l2.4 5.3 5.6.5-4.3 3.8 1.3 5.6L9 13.3 4 16.2l1.3-5.6L1 6.8l5.6-.5z"/></g></svg></div>
    </article>

    <h2 class="abs section-title" style="left:808px;top:1477px">CATEGORIES</h2>
    <ul class="abs catlist">
      <li><svg width="5" height="8"><path d="M0 0l5 4-5 4z" fill="#777"/></svg>Phasellus felis dolor scelerisque</li>
      <li><svg width="5" height="8"><path d="M0 0l5 4-5 4z" fill="#777"/></svg>Tempus eget lobortis id libero.</li>
      <li><svg width="5" height="8"><path d="M0 0l5 4-5 4z" fill="#777"/></svg>Aliquam nec erat at purus cursus</li>
      <li><svg width="5" height="8"><path d="M0 0l5 4-5 4z" fill="#777"/></svg>Vestibulum ligula augue</li>
      <li><svg width="5" height="8"><path d="M0 0l5 4-5 4z" fill="#777"/></svg>Bibendum accumsan vestibulum</li>
      <li><svg width="5" height="8"><path d="M0 0l5 4-5 4z" fill="#777"/></svg>Phasellus felis dolor scelerisque</li>
      <li><svg width="5" height="8"><path d="M0 0l5 4-5 4z" fill="#777"/></svg>Tempus eget lobortis id libero.</li>
      <li><svg width="5" height="8"><path d="M0 0l5 4-5 4z" fill="#777"/></svg>Aliquam nec erat at purus cursus</li>
    </ul>
  </section>

  <footer class="abs footer">
    <div class="abs about" style="left:81px;top:42px">
      <h2 class="section-title">ABOUT</h2>
      <p>Aenean nonummy hendrerit mauris. Phasellus porta. Fusce suscipit varius mi. Cum sociis natoque penatibu s et magnis dis parturient montes, nascetur ridiculus mus. Nulla dui. Fusce feugiat malesuada odio. Morbi nunc odio, gravidaat. Nulla dui. Fusce feugiat malesua da odio. Morbi nunc odio, gravida at, cursus nec. Duis ultricies pharetra magna.</p>
    </div>
    <div class="abs news" style="left:506px;top:42px">
      <h2 class="section-title">TRAVEL NEWS</h2>
      <div class="news-item"><div class="thumb" role="img" aria-label="Beach holiday snapshot" style="background:linear-gradient(160deg,#6fb7e0,#d9a869)"></div><div><b>Phasellus porta.</b><span>Fusce suscipit varius mi.</span><span>Cum sociis noque pen</span></div></div>
      <div class="news-item" style="margin-top:20px"><div class="thumb" role="img" aria-label="Seaside resort building" style="background:linear-gradient(180deg,#8fb6d8,#b08a5e)"></div><div><b>Phasellus porta.</b><span>Fusce suscipit varius mi.</span><span>Cum sociis noque pen</span></div></div>
    </div>
    <div class="abs follow" style="left:828px;top:42px">
      <h2 class="section-title">FOLLOW US</h2>
      <address>14 Via Lattea, Milan, 20121.</address>
      <div class="phone">+1 800 555 0142</div>
      <div class="dots"><span style="background:#3b5998"></span><span style="background:#333"></span><span style="background:#2ea3e6"></span><span style="background:#0e76a8"></span></div>
    </div>
  </footer>

  <div class="abs bottom"><span>Terms and Conditions | Privacy Policy | FAQ's</span><span>Copyright © 2014. All Rights Reserved.</span></div>
</div>
</body>
</html>
```